Brightwell Pictures Business Card

Hello,

i would like to have a dynamic, creative but tasteful card, colour used, front and back. I have attached a sample card that I liked very much from another individual to give you an idea of the theme/approach, but not colour. Ideally the graphic elements of the Brightwell Logo are brought into the design.

Target Market(s)

North America

Industry/Entity Type

Film Production

Contact Information for Business Card

Mirela Vantasch
President/Founder
Brightwell Pictures Inc.
587 914 3362
mirela@brightwellpix.tv

Font styles to use
Sans Serif

Colors
6b449b
5c5c5c
fdfdfd
000000

Requirements
Must have
• Logo, name, Company name, email and cell number. no Address line to be included.
Should not have
• any unrelated GFX elements, serif fonts

```html
<!DOCTYPE html>
<html lang="en">
<head>
<meta charset="utf-8">
<title>Brightwell Pictures Business Card</title>
<link href="https://fonts.googleapis.com/css2?family=Lato:wght@400;700;900&display=swap" rel="stylesheet">
<style>
  :root {
    --purple: #6b449b;
    --lavender: #9b85c0;
    --grey: #5c5c5c;
    --paper: #fdfdfd;
    --ink: #000000;
    --backdrop: #e9e8ec;
  }
  html, body {
    margin: 0;
    width: 1200px;
    height: 1200px;
    overflow: hidden;
    background: var(--backdrop);
    font-family: "Lato", sans-serif;
  }
  .card {
    position: absolute;
    left: 220px;
    width: 760px;
    height: 434px;
    background: var(--paper);
    border-radius: 30px;
    overflow: hidden;
    box-shadow: 0 10px 30px rgba(0,0,0,0.18);
  }
  .card--front { top: 110px; }
  .card--back { top: 650px; }
  .card__shape {
    position: absolute;
    inset: 0;
    width: 100%;
    height: 100%;
  }
  .wordmark {
    position: absolute;
    display: flex;
    align-items: center;
    gap: 14px;
    font-weight: 900;
    color: var(--purple);
    letter-spacing: -1px;
    line-height: 1;
  }
  .wordmark__dot {
    border-radius: 50%;
    background: var(--grey);
  }
  .card--front .wordmark {
    left: 250px;
    top: 168px;
    font-size: 84px;
  }
  .card--front .wordmark__dot { width: 30px; height: 30px; }
  .contact {
    position: absolute;
    left: 60px;
    top: 120px;
    width: 420px;
    color: var(--ink);
  }
  .contact__name {
    margin: 0;
    font-size: 34px;
    font-weight: 400;
    line-height: 1.1;
  }
  .contact__role,
  .contact__company {
    margin: 4px 0 0;
    font-size: 20px;
    line-height: 1.2;
  }
  .contact__rule {
    height: 0;
    border-top: 2px solid var(--ink);
    margin: 16px 0 14px;
  }
  .contact__row {
    display: flex;
    align-items: center;
    gap: 12px;
    font-size: 19px;
    margin-bottom: 8px;
  }
  .contact__icon { width: 22px; height: 22px; flex: none; }
  .card--back .wordmark {
    left: 250px;
    top: 350px;
    font-size: 58px;
  }
  .card--back .wordmark__dot { width: 22px; height: 22px; }
</style>
</head>
<body>

<section class="card card--front" aria-label="Card front">
  <svg class="card__shape" viewBox="0 0 760 434" aria-hidden="true">
    <path d="M0,95 C40,300 230,425 440,434 L0,434 Z" fill="var(--purple)"/>
  </svg>
  <div class="wordmark"><span>Brightwell</span><span class="wordmark__dot"></span></div>
</section>

<section class="card card--back" aria-label="Card back">
  <svg class="card__shape" viewBox="0 0 760 434" aria-hidden="true">
    <circle cx="650" cy="130" r="190" fill="none" stroke="var(--lavender)" stroke-width="34"/>
  </svg>

  <div class="contact">
    <h1 class="contact__name">Mirela Vantasch</h1>
    <p class="contact__role">Founder</p>
    <p class="contact__company">Brightwell Pictures Inc.</p>
    <div class="contact__rule"></div>
    <div class="contact__row">
      <svg class="contact__icon" viewBox="0 0 24 24" aria-hidden="true">
        <circle cx="12" cy="12" r="10.5" fill="none" stroke="var(--ink)" stroke-width="1.8"/>
        <path d="M8.5 7.5c-.8.8-.8 2.6.9 4.8 1.7 2.2 3.8 3.6 5.1 3.2l1-1.1-1.8-1.6-1 .7c-.9-.4-2-1.6-2.4-2.5l.7-1-1.5-1.9z" fill="var(--ink)"/>
      </svg>
      <span>: 587 914 3362</span>
    </div>
    <div class="contact__row">
      <svg class="contact__icon" viewBox="0 0 24 24" aria-hidden="true">
        <rect x="2" y="5" width="20" height="14" fill="var(--ink)"/>
        <path d="M2.5 5.5 12 13l9.5-7.5" fill="none" stroke="var(--paper)" stroke-width="1.6"/>
      </svg>
      <span>: mirela@brightwellpix.tv</span>
    </div>
  </div>

  <div class="wordmark"><span>Brightwell</span><span class="wordmark__dot"></span></div>
</section>

</body>
</html>
```